aesthetic packaging for down comforter company

Hi guys,

I'm looking for a creative, aesthetic, serious, premium & luxury package design for a down comforter product. The box will be 50cm x 25cm x 25 cm.

please use our logo as reference to show how premium our product is

A small description of what is our product. It is a downcomforter blanket that caters to ALL-SEASONS. Size will be both Queen and King. So please add an option where it can be marked as one of the options.

It is a baffle box design. The product is DESIGNED IN AUSTRALIA, please add this key point

Down is a natural material and the higher the Down content, the lighter and softer the product. Down differs considerably from feathers, as it does not have the hard quill shafts that is common to feather. It is the fluffy filament which comes from the breast of a duck and is an extremely efficient natural insulator.

Target Market(s)

mothers,moms, ladies,girls

Requirements
Nice to have
• feathers, beds ,linen, anything to do with bedding if possible. Try to minimize pictures

```html
<!DOCTYPE html>
<html lang="en">
<head>
<meta charset="utf-8">
<title>Velora Down Comforter – Box Dieline</title>
<link rel="stylesheet" href="https://fonts.googleapis.com/css2?family=Montserrat:ital,wght@0,400;0,500;0,700;1,700&display=swap">
<style>
  :root {
    --stage: #4d4d4d;
    --gold: #b08a3e;
    --gold-light: #d6b061;
    --gold-deep: #9c7628;
    --satin-light: #ffffff;
    --satin-mid: #f1efe8;
    --satin-shade: #dcd8cc;
  }
  html, body {
    margin: 0;
    width: 1200px;
    height: 743px;
    overflow: hidden;
    background: var(--stage);
  }
  .dieline {
    position: absolute;
    left: 260px;
    top: 14px;
    width: 680px;
    height: 714px;
    display: block;
  }
  .brand { font-family: "Montserrat", sans-serif; font-weight: 500; fill: var(--gold); letter-spacing: 1px; }
  .headline { font-family: "Montserrat", sans-serif; font-weight: 400; fill: var(--gold); font-size: 15px; letter-spacing: .5px; }
  .headline-strong { font-family: "Montserrat", sans-serif; font-weight: 700; font-style: italic; fill: var(--gold); font-size: 11.5px; }
  .tagline { font-family: "Montserrat", sans-serif; font-weight: 400; fill: #444; font-size: 9px; }
  .body-copy { font-family: "Montserrat", sans-serif; font-weight: 400; fill: #555; font-size: 5.6px; }
  .origin { font-family: "Montserrat", sans-serif; font-weight: 400; fill: #444; font-size: 6px; letter-spacing: .4px; }
  .copy-frame { fill: none; stroke: var(--gold-light); stroke-width: .8; }
  .gold-band { fill: var(--gold); }
  .sweep { fill: none; stroke: var(--gold); stroke-width: 3; }
</style>
</head>
<body>
<svg class="dieline" viewBox="35 25 850 893" xmlns="http://www.w3.org/2000/svg">
  <defs>
    <linearGradient id="satin" gradientUnits="userSpaceOnUse" x1="35" y1="25" x2="885" y2="918">
      <stop offset="0" stop-color="var(--satin-mid)"/>
      <stop offset=".3" stop-color="var(--satin-light)"/>
      <stop offset=".55" stop-color="var(--satin-shade)"/>
      <stop offset=".75" stop-color="var(--satin-light)"/>
      <stop offset="1" stop-color="var(--satin-mid)"/>
    </linearGradient>
    <linearGradient id="featherTone" x1="0" y1="0" x2="1" y2="1">
      <stop offset="0" stop-color="var(--gold-light)"/>
      <stop offset="1" stop-color="var(--gold-deep)"/>
    </linearGradient>
    <clipPath id="mainBand"><rect x="277" y="270" width="608" height="402"/></clipPath>
  </defs>

  <!-- satin surface across every panel -->
  <g class="box-panels" role="img" aria-label="White satin fabric background" fill="url(#satin)">
    <path class="top-tuck" d="M277 270 V60 Q277 25 312 25 H445 Q480 25 480 60 V270 Z"/>
    <polygon class="top-dust-left" points="90,80 265,80 275,270 78,270"/>
    <polygon class="top-dust-right" points="492,80 667,80 680,270 482,270"/>
    <path class="side-panel" d="M35 305 Q35 270 70 270 H277 V672 H70 Q35 672 35 637 Z"/>
    <rect class="front-band" x="277" y="270" width="608" height="402"/>
    <path class="bottom-tuck" d="M277 672 H480 V883 Q480 918 445 918 H312 Q277 918 277 883 Z"/>
    <polygon class="bottom-dust-left" points="75,672 275,672 265,865 90,865"/>
    <polygon class="bottom-dust-right" points="482,672 680,672 667,865 492,865"/>
  </g>

  <!-- gold edge bands -->
  <rect class="gold-band" x="277" y="267" width="203" height="6"/>
  <rect class="gold-band" x="480" y="268" width="405" height="6"/>
  <rect class="gold-band" x="277" y="664" width="608" height="6"/>

  <!-- top tuck flap brand -->
  <text class="brand" font-size="22" transform="translate(378 122) rotate(180)" text-anchor="middle">VELORA</text>

  <!-- side panel -->
  <text class="brand" font-size="20" transform="translate(210 345) rotate(-90)" text-anchor="middle">VELORA</text>
  <text class="headline" transform="translate(114 650) rotate(-90)">DOWN IS A NATURAL</text>
  <text class="headline-strong" transform="translate(128 650) rotate(-90)">MATERIAL AND THE HIGHER</text>
  <text class="headline-strong" transform="translate(141 650) rotate(-90)">THE DOWN CONTENT,</text>
  <text class="tagline" transform="translate(157 650) rotate(-90)">the lighter and softer</text>
  <text class="tagline" transform="translate(169 650) rotate(-90)">the product.</text>
  <rect class="copy-frame" x="183" y="408" width="45" height="242"/>
  <g class="body-copy">
    <text transform="translate(194 644) rotate(-90)">Down differs considerably from feathers, as it does not have the</text>
    <text transform="translate(203 644) rotate(-90)">hard quill shafts that is common to feather. It is the fluffy filament</text>
    <text transform="translate(212 644) rotate(-90)">which comes from the breast of a duck and is an extremely</text>
    <text transform="translate(221 644) rotate(-90)">efficient natural insulator.</text>
  </g>
  <text class="origin" transform="translate(259 650) rotate(-90)">DESIGNED IN AUSTRALIA</text>
  <text class="brand" font-size="15" x="333" y="648" text-anchor="middle">VELORA</text>

  <!-- front panel -->
  <g clip-path="url(#mainBand)">
    <ellipse class="sweep" cx="665" cy="470" rx="215" ry="190" transform="rotate(-12 665 470)"/>
    <ellipse class="sweep" cx="640" cy="470" rx="185" ry="182" transform="rotate(8 640 470)"/>
  </g>
  <g class="feathers" role="img" aria-label="Gold feather illustrations" fill="url(#featherTone)">
    <ellipse cx="345" cy="410" rx="34" ry="120" transform="rotate(18 345 410)"/>
    <ellipse cx="428" cy="488" rx="26" ry="80" transform="rotate(14 428 488)"/>
    <ellipse cx="735" cy="452" rx="28" ry="95" transform="rotate(-14 735 452)"/>
    <ellipse cx="815" cy="525" rx="36" ry="125" transform="rotate(-20 815 525)"/>
  </g>
  <text class="brand" font-size="30" transform="translate(638 462) rotate(-90)" text-anchor="middle">VELORA</text>
  <text class="brand" font-size="15" x="825" y="358" text-anchor="middle">VELORA</text>
</svg>
</body>
</html>
```